Notepads for Marketing pieces-BOLD design

Looking for notepads for marketing pieces with logo, phone number, and website. Maybe something faded in background. Looking for bold and different

```html
<!DOCTYPE html>
<html lang="en">
<head>
<meta charset="utf-8">
<title>Vitalcrest Notepad Pages</title>
<link rel="stylesheet" href="https://fonts.googleapis.com/css2?family=Poppins:wght@500;600;800&family=Montserrat:wght@400&display=swap">
<style>
  :root {
    --backdrop: #6a6a6a;
    --paper: #f4f4f4;
    --brand-red: #e3282c;
    --ink: #222222;
    --footer-ink: #3a3a3a;
    --watermark: rgba(0, 0, 0, 0.045);
  }
  * { margin: 0; padding: 0; box-sizing: border-box; }
  html, body {
    width: 1200px;
    height: 780px;
    overflow: hidden;
    background: var(--backdrop);
  }
  .spread {
    position: absolute;
    left: 150px;
    top: 76px;
    display: flex;
    gap: 10px;
  }
  .notepad-page {
    position: relative;
    width: 445px;
    height: 628px;
    background: var(--paper);
    overflow: hidden;
    box-shadow: 0 4px 10px rgba(0, 0, 0, 0.25);
  }
  .page-watermark {
    position: absolute;
    left: -40px;
    top: 330px;
    font-family: "Poppins", sans-serif;
    font-weight: 800;
    font-size: 118px;
    letter-spacing: 4px;
    color: var(--watermark);
    transform: rotate(-42deg);
    transform-origin: left center;
    white-space: nowrap;
    pointer-events: none;
  }
  .letterhead {
    position: absolute;
    left: 22px;
    top: 44px;
  }
  .brand-name {
    margin-left: 10px;
    font-family: "Poppins", sans-serif;
    font-weight: 800;
    font-size: 26px;
    letter-spacing: 1px;
    line-height: 1;
    color: var(--brand-red);
  }
  .service-line {
    margin-top: 14px;
    font-family: "Poppins", sans-serif;
    font-weight: 600;
    font-size: 6.6px;
    color: var(--ink);
    white-space: nowrap;
  }
  .page-footer {
    position: absolute;
    right: 26px;
    bottom: 14px;
    display: flex;
    align-items: center;
    gap: 4px;
    font-family: "Montserrat", sans-serif;
    font-size: 11.5px;
    color: var(--footer-ink);
  }
  .page-footer svg { width: 10px; height: 10px; fill: var(--brand-red); }
  .page-footer .web-icon { margin-left: 4px; }
</style>
</head>
<body>
  <main class="spread">
    <section class="notepad-page">
      <div class="page-watermark" aria-hidden="true">VITALCREST</div>
      <header class="letterhead">
        <div class="brand-name">VITALCREST</div>
        <p class="service-line">Home Health | Medical Staffing | Outpatient Therapy</p>
      </header>
      <footer class="page-footer">
        <svg viewBox="0 0 24 24" aria-hidden="true"><path d="M3 9c0-3 4-5 9-5s9 2 9 5v2h-5V9c-1-1-7-1-8 0v2H3zM6 12h12l3 8H3z"/></svg>
        <span>123-456-7890</span>
        <svg class="web-icon" viewBox="0 0 24 24" aria-hidden="true"><circle cx="12" cy="12" r="10"/></svg>
        <span>vitalcrest.org</span>
      </footer>
    </section>
    <section class="notepad-page">
      <div class="page-watermark" aria-hidden="true">VITALCREST</div>
      <header class="letterhead">
        <div class="brand-name">VITALCREST</div>
        <p class="service-line">Home Health | Medical Staffing | Outpatient Therapy</p>
      </header>
      <footer class="page-footer">
        <svg viewBox="0 0 24 24" aria-hidden="true"><path d="M3 9c0-3 4-5 9-5s9 2 9 5v2h-5V9c-1-1-7-1-8 0v2H3zM6 12h12l3 8H3z"/></svg>
        <span>123-456-7890</span>
        <svg class="web-icon" viewBox="0 0 24 24" aria-hidden="true"><circle cx="12" cy="12" r="10"/></svg>
        <span>vitalcrest.org</span>
      </footer>
    </section>
  </main>
</body>
</html>
```